Unique Elegant Stationary Set

Prepare a unique eye catching stationary set consisting of :
(1) Letterhead
(2) A3 Envelope
(3) Business Card
(4) Email Signature Banner

Package to be elegant, modern, and designers not only to think of design or colors but also materials could make a big difference, embossing, debossing, glossy, matt ....etc.

I attached both our new logos (Stacked or Linear) noting you may use any of them but you cant modify anything in the logos. Also attached our final draft portfolio to see what type of projects we work on and i also have here a glimboard page link showing the direction we want: https://www.glimboard.example/ravelkoton/business-card-design/

Target Market(s)

VVIP / Elite Developers

Industry/Entity Type

Architecture

Font styles to use
Sans Serif
Other font styles liked:
• unitext

Requirements
Should not have
• too many colors, or being busy in general. We want something pleasing to the eye

```html
<!DOCTYPE html>
<html lang="en">
<head>
<meta charset="utf-8">
<title>Kavro Stationery Set</title>
<link rel="stylesheet" href="https://fonts.googleapis.com/css2?family=Playfair+Display:ital,wght@1,600&family=Roboto+Condensed:wght@300;700&family=Arimo:wght@400;700&family=Montserrat:wght@400;500;800&display=swap">
<style>
:root{
  --bg:#d3d8db;
  --red:#c8192b;
  --ink:#1a1a1a;
  --grey:#5b5b5b;
  --rule:#8a8a8a;
  --paper:#ffffff;
  --night:#16171f;
  --label:#ffffff;
}
*{box-sizing:border-box;margin:0;padding:0}
html,body{width:1200px;height:984px;overflow:hidden;background:var(--bg)}
.board{position:relative;width:1200px;height:984px;background:radial-gradient(circle at 60% 40%,#e2e6e8,var(--bg))}
.abs{position:absolute}
.section-label{position:absolute;font-family:"Playfair Display",serif;font-style:italic;font-weight:600;font-size:35px;color:var(--label);text-shadow:0 2px 3px rgba(0,0,0,.35);transform:translateX(-50%);white-space:nowrap;letter-spacing:1px}
.sheet{position:absolute;background:var(--paper);box-shadow:0 8px 18px rgba(0,0,0,.25);overflow:hidden}
.band{position:absolute;left:0;right:0;bottom:0;background:var(--red)}
.brand{position:absolute;display:flex;align-items:center;gap:6px;font-family:"Montserrat",sans-serif;font-weight:800;color:var(--red);letter-spacing:2px;line-height:1;white-space:nowrap}
.brand::after{content:"";display:block;background:var(--red)}
.brand.md{font-size:30px}.brand.md::after{width:7px;height:7px}
.brand.lg{font-size:38px}.brand.lg::after{width:8px;height:8px}
.brand.sm{font-size:20px;color:#fff}.brand.sm::after{width:5px;height:5px;background:#fff}
.center-x{left:50%;transform:translateX(-50%)}
.row{position:absolute;display:flex;align-items:center;gap:4px;white-space:nowrap}
.ico{width:1em;height:1em;fill:var(--red);flex:none}
.env-line{font-family:"Arimo",sans-serif;font-size:7.5px;color:var(--ink)}
.first{font-weight:700;color:var(--red)}
.last{font-weight:300}
/* letterhead */
.lh-name{font-family:"Roboto Condensed",sans-serif;font-size:23px;color:var(--grey);line-height:1}
.lh-role{font-family:"Arimo",sans-serif;font-weight:700;font-size:9px;color:var(--ink)}
.lh-contact{font-family:"Arimo",sans-serif;font-size:8.5px;color:var(--ink)}
.lh-body{position:absolute;left:24px;width:409px;font-family:"Arimo",sans-serif;font-size:9.8px;line-height:13px;color:var(--ink);text-align:justify}
.lh-date{font-family:"Arimo",sans-serif;font-weight:700;font-size:11px;color:var(--ink)}
.foot-text{font-family:"Montserrat",sans-serif;font-size:9.5px;color:var(--ink)}
/* business card */
.bc-name{font-family:"Montserrat",sans-serif;font-size:21px;color:#8d8f96;line-height:1}
.bc-name .first{font-weight:500}
.bc-name .last{font-weight:400}
.bc-text{font-family:"Montserrat",sans-serif;font-size:11.5px;color:#fff}
.sig-name{font-family:"Montserrat",sans-serif;font-size:20px;color:var(--red);line-height:1}
.sig-name .first{font-weight:500}
.sig-name .last{font-weight:400}
.sig-text{font-family:"Montserrat",sans-serif;font-size:9px;color:var(--ink)}
.dot{width:7px;height:7px;border-radius:50%;background:var(--red);display:inline-block}
</style>
</head>
<body>
<svg width="0" height="0" style="position:absolute">
  <symbol id="i-phone" viewBox="0 0 24 24"><path d="M6.6 10.8a15.1 15.1 0 0 0 6.6 6.6l2.2-2.2c.3-.3.7-.4 1-.2 1.1.4 2.3.6 3.6.6.6 0 1 .4 1 1V20c0 .6-.4 1-1 1A17 17 0 0 1 3 4c0-.6.4-1 1-1h3.5c.6 0 1 .4 1 1 0 1.3.2 2.5.6 3.6.1.3 0 .7-.2 1z"/></symbol>
  <symbol id="i-globe" viewBox="0 0 24 24"><path d="M12 2a10 10 0 1 0 0 20 10 10 0 0 0 0-20zm-1 17.9A8 8 0 0 1 4.1 11L9 16v1a2 2 0 0 0 2 2zm6.9-2.5A2 2 0 0 0 16 16h-1v-3a1 1 0 0 0-1-1H8v-2h2a1 1 0 0 0 1-1V7h2a2 2 0 0 0 2-2v-.4a8 8 0 0 1 2.9 12.8z"/></symbol>
  <symbol id="i-mail" viewBox="0 0 24 24"><path d="M3 6h18v12H3zm2 2v.5l7 4.5 7-4.5V8l-7 4.5z"/></symbol>
  <symbol id="i-pin" viewBox="0 0 24 24"><path d="M12 2a7 7 0 0 0-7 7c0 5.2 7 13 7 13s7-7.8 7-13a7 7 0 0 0-7-7zm0 9.5a2.5 2.5 0 1 1 0-5 2.5 2.5 0 0 1 0 5z"/></symbol>
</svg>

<main class="board">
  <div class="section-label" style="left:320px;top:18px">Envelope Design</div>
  <div class="section-label" style="left:808px;top:26px">Letterhead</div>
  <div class="section-label" style="left:326px;top:922px">Business card</div>
  <div class="section-label" style="left:780px;top:922px">Email Signature</div>

  <!-- envelope front -->
  <section class="sheet envelope-front" style="left:141px;top:77px;width:389px;height:172px">
    <div class="brand md center-x" style="top:92px">KAVRO</div>
    <div class="abs" style="left:0;right:0;top:128px;height:1px;background:var(--rule)"></div>
    <div class="row env-line center-x" style="top:135px"><svg class="ico"><use href="#i-pin"/></svg>12 Orchard Lane, Milbrook, Kent, ME4 2TQ</div>
    <div class="row env-line" style="left:41px;top:148px"><svg class="ico"><use href="#i-phone"/></svg>&nbsp;(555) 014-2758</div>
    <div class="row env-line" style="left:133px;top:148px"><svg class="ico"><use href="#i-mail"/></svg>&nbsp;info@kavro.example</div>
    <div class="row env-line" style="left:256px;top:148px"><svg class="ico"><use href="#i-globe"/></svg>www.kavro.example</div>
    <div class="band" style="height:8px"></div>
  </section>

  <!-- envelope back -->
  <section class="sheet envelope-back" style="left:141px;top:268px;width:389px;height:173px;background:var(--red)">
    <svg class="abs" style="left:0;top:0" width="389" height="60" viewBox="0 0 389 60">
      <path d="M4 0h385v45q0 13-13 13H17Q5 58 4 45z" fill="#d01c2e" style="filter:drop-shadow(0 4px 5px rgba(0,0,0,.3))"/>
    </svg>
    <div class="brand sm center-x" style="top:20px">KAVRO</div>
  </section>

  <!-- debossed pattern panel -->
  <div class="sheet pattern" role="img" aria-label="Dark debossed surface with a repeating brand pattern and one red accent mark" style="left:137px;top:452px;width:394px;height:226px;background:linear-gradient(180deg,#22232b,#15161c)"></div>

  <!-- business card -->
  <section class="sheet business-card" style="left:137px;top:700px;width:394px;height:225px;background:var(--night)">
    <div class="brand lg center-x" style="top:20px">KAVRO</div>
    <div class="bc-name abs" style="left:26px;top:136px"><span class="first" style="color:var(--red)">Mara</span> <span class="last">Tellen</span></div>
    <div class="bc-text abs" style="left:90px;top:157px">Founder &amp; CEO</div>
    <div class="abs" style="left:196px;top:127px;width:2px;height:56px;background:var(--red)"></div>
    <div class="row bc-text" style="left:216px;top:135px;gap:8px"><svg class="ico"><use href="#i-phone"/></svg>(555) 014-2758</div>
    <div class="row bc-text" style="left:216px;top:150px;gap:8px"><svg class="ico"><use href="#i-globe"/></svg>hello@kavro.example</div>
    <div class="row bc-text" style="left:216px;top:164px;gap:8px"><svg class="ico"><use href="#i-mail"/></svg>www.kavro.example</div>
    <div class="bc-text abs center-x" style="top:193px;white-space:nowrap">880 Linden Ave. Suite 300 Fairhaven, TX 75001</div>
    <div class="band" style="height:10px"></div>
  </section>

  <!-- letterhead -->
  <section class="sheet letterhead" style="left:577px;top:79px;width:457px;height:645px">
    <div class="brand md center-x" style="top:27px">KAVRO</div>
    <div class="abs" style="left:24px;right:24px;top:62px;height:1px;background:var(--rule)"></div>
    <div class="abs" style="left:154px;width:149px;top:61px;height:3px;background:var(--red)"></div>

    <div class="lh-name abs" style="left:24px;top:127px"><span class="first">Mara</span> <span class="last">Tellen</span></div>
    <div class="lh-role abs" style="left:25px;top:150px">Founder &amp; CEO</div>
    <div class="lh-date abs" style="right:24px;top:134px">August-05-2019</div>
    <div class="row lh-contact" style="left:24px;top:173px"><svg class="ico"><use href="#i-phone"/></svg>(555) 019-7777</div>
    <div class="row lh-contact" style="left:24px;top:184px"><svg class="ico"><use href="#i-globe"/></svg>www.kavro.example</div>
    <div class="row lh-contact" style="left:24px;top:195px"><svg class="ico"><use href="#i-mail"/></svg>hello@kavro.example</div>

    <p class="lh-body" style="top:226px">Lorem ipsum dolor sit amet, consectetuer adipiscing elit, sed diam nonummy nibh euismod tincidunt ut laoreet dolore magna aliquam erat volutpat. Ut wisi enim ad minim veniam, quis nostrud exerci tation ullamcorper suscipit lobortis</p>
    <p class="lh-body" style="top:278px">Lorem ipsum dolor sit amet, cons ectetuer adipiscing elit, sed diam nonummy nibh euismod tincidunt ut laoreet dolore magna aliquam erat volutpat. Ut wisi enim ad minim veniam, quis nostrud exerci tation ullamcorper suscipit lobortis nisl ut aliquip ex ea commodo consequat. Lorem ipsum dolor sit amet, consectetuer olutpat. Ut wisi enim ad minim veniam, quis nostrud exerci tation ullamcorper suscipit lobortis nisl ut aliquip ex ea commodo consequat. Duis autem</p>
    <p class="lh-body" style="top:369px">vel eum iriure dolor in hendrerit in vulputate velit esse molestie consequat, vel illum dolore eu feugiat nulla facilisis at vero eros et accumsan et iusto odio dignissim qui blandit praesent luptatum zzril delenit augue duis dolore te feugait nulla facilisi. Lorem ipsum dolor sit amet, cons ectetuer adipiscing elit, sed diam nonummy nibh euismod tincidunt ut laoreet dolore magna aliquam erat volutpat. Ut wisi enim .</p>

    <div class="abs" role="img" aria-label="Handwritten signature of the director" style="left:24px;top:451px;width:155px;height:48px;background:linear-gradient(90deg,#f2f2f3,#e6e6e8);border-radius:4px"></div>
    <div class="lh-name abs" style="left:24px;top:505px;font-size:21px"><span class="first">Ines</span> <span class="last">Varga</span></div>
    <div class="lh-role abs" style="left:26px;top:527px">Director</div>

    <div class="abs" style="left:0;right:0;top:580px;height:1px;background:var(--rule)"></div>
    <div class="row foot-text center-x" style="top:588px"><svg class="ico"><use href="#i-pin"/></svg>&nbsp;880 Linden Ave. Suite 300, Fairhaven, TX 75001</div>
    <div class="row foot-text" style="left:30px;top:610px"><svg class="ico"><use href="#i-phone"/></svg>&nbsp;(555) 014-2758</div>
    <div class="row foot-text" style="left:150px;top:611px"><svg class="ico"><use href="#i-mail"/></svg>&nbsp;hello@kavro.example</div>
    <div class="row foot-text" style="left:303px;top:611px"><svg class="ico"><use href="#i-globe"/></svg>&nbsp;www.kavro.example</div>
    <div class="band" style="height:13px"></div>
  </section>

  <!-- email signature -->
  <section class="sheet email-signature" style="left:577px;top:754px;width:468px;height:156px">
    <div class="brand lg" style="right:20px;top:22px">KAVRO</div>
    <div class="sig-name abs" style="left:19px;top:53px"><span class="first">Mara</span> <span class="last">Tellen</span></div>
    <div class="sig-text abs" style="left:19px;top:73px">Founder &amp; CEO</div>
    <div class="row sig-text" style="left:19px;top:91px;gap:6px"><svg class="ico"><use href="#i-phone"/></svg>(555) 014-2758</div>
    <div class="row sig-text" style="left:19px;top:103px;gap:6px"><svg class="ico"><use href="#i-globe"/></svg>hello@kavro.example</div>
    <div class="row sig-text" style="left:19px;top:115px;gap:6px"><svg class="ico"><use href="#i-mail"/></svg>www.kavro.example</div>
    <div class="row sig-text" style="left:19px;top:127px;gap:6px"><svg class="ico"><use href="#i-pin"/></svg>880 Linden Ave. Suite 300, Fairhaven, TX 75001</div>
    <div class="row sig-text" style="left:348px;top:135px;gap:5px">Follow us <span class="dot"></span><span class="dot"></span><span class="dot"></span><span class="dot"></span><span class="dot"></span></div>
    <div class="band" style="height:8px"></div>
  </section>
</main>
</body>
</html>
```